Lanternwell Cybersecurity Web Site Project

Lanternwell Cybersecurity is an MSP provider that is a full-service IT delivery organization focused on service deliver and information security.

We are looking for CREATIVE and UNIQUE website design that lays out the initial landing page and content page for us to continue developing for our organization. We have attached a .zip of our logo and images stock for you to incorporate into the site.

We are a Cybersecurity / MSP focused on providing a full-service outsourced IT Services to organizations that also have information cybersecurity compliance requirements such as HIPAA, PCI-DSS,
NYS DFS 23 NYCRR 500.

Systems / Applications Solutions:
On-Premises and Cloud Solutions
IT Services / Help Desk
User and System Issue Resolution
Office365 Administration
Azure / Cloud Virtualization
Windows / Linux Server Administration

We are looking for two (2) .psd design files for the landing page and content page based on the logo stock art provided and all files / artwork created by the designer at project completion.

Please be creative and make this site stand out from all others. We are well aware of template sites like Layout Grove and others like it, so please we are not looking for a template we could download ourselves.

Target Market(s)

Demographic: Law Firms, Legal Services, Small - Medium Doctor offices, Medical services companies, Finance, Mortgage, Securities.

Businesses looking to outsource their IT departments.
Move to a full cloud business solution.
Require cybersecurity compliance such as HIPAA, PCI-DSS or DFS 23 NYCRR 500.

Industry/Entity Type

Information Technology

Number of Pages Required

2 page

Requirements
Must have
• We have included stock art for logo's, banners, headers, footers, please use that graphic stock for the site.

We operate in the Managed Service Provider (MSP) and Cybersecurity space
Should not have
• Themes we can get from any of the theme sites out there. We are looking for something completely new and unique.

```html
<!DOCTYPE html>
<html lang="en">
<head>
<meta charset="utf-8">
<title>Lanternwell Cybersecurity</title>
<link href="https://fonts.googleapis.com/css2?family=Krona+One&family=Montserrat:wght@400;500;600;700&display=swap" rel="stylesheet">
<style>
:root{
  --red-deep:#3d0206;
  --red:#8e0a0f;
  --red-bright:#b3141a;
  --navy:#1b1f4a;
  --ink:#222;
  --grey-bg:#ececec;
  --dark:#1c1c1f;
  --black:#0b0b0b;
  --white:#fff;
  --silver:#c9c9cc;
  --bezel:#0e0e10;
}
*{box-sizing:border-box;margin:0;padding:0}
html,body{width:1200px;height:3369px;overflow:hidden}
body{font-family:"Montserrat",sans-serif;color:var(--ink);background:var(--white);position:relative}
.display{font-family:"Krona One",sans-serif;text-transform:uppercase;letter-spacing:1px}
section,header,footer{position:absolute;left:0;width:1200px;overflow:hidden}
.abs{position:absolute}

/* header / nav */
.brand{display:flex;align-items:center;gap:10px;color:var(--white);font-weight:700;font-size:15px;letter-spacing:1px;text-transform:uppercase;line-height:1.1}
.brand-mark{width:34px;height:34px;background:var(--red-bright);flex:none}
.nav{display:flex;align-items:center;gap:28px;font-size:13px;color:var(--white);text-transform:uppercase}
.nav .active{font-weight:700}
.nav .pill{border:1.5px solid var(--white);border-radius:16px;padding:6px 20px;font-weight:600}

/* device frames */
.laptop-screen{position:absolute;background:var(--bezel);border:2px solid #8a8a8e;border-radius:14px 14px 0 0;padding:18px 14px 24px}
.laptop-screen .fill{width:100%;height:100%}
.laptop-base{position:absolute;height:14px;background:linear-gradient(180deg,#e4e4e6,#9a9a9e);border-radius:0 0 10px 10px}

/* hero */
.hero{top:0;height:661px;background:radial-gradient(ellipse at 30% 90%,#b5121a 0%,#7a0509 45%,var(--red-deep) 100%)}
.hero-eyebrow{left:59px;top:256px;color:var(--white);font-size:20px;letter-spacing:.5px;text-transform:uppercase}
.hero-title{left:59px;top:280px;color:var(--white);font-size:54px;letter-spacing:2px}
.hero-copy{left:59px;top:358px;width:560px;color:var(--white);font-size:13.5px;line-height:20px}
.btn{display:flex;align-items:center;justify-content:center;font-size:13px;font-weight:600;text-transform:uppercase;color:var(--white)}
.btn-solid{left:63px;top:458px;width:155px;height:37px;background:#111}
.btn-line{left:243px;top:458px;width:155px;height:37px;border:1.5px solid var(--white)}

/* partner bar */
.partners{top:661px;height:89px;background:var(--dark);display:flex;align-items:center;justify-content:space-between;padding:0 59px}
.partner{display:flex;align-items:center;gap:8px;color:#e6e6e6;font-size:21px;font-weight:600;letter-spacing:.5px}
.partner i{width:20px;height:20px;border-radius:50%;border:2px solid #e6e6e6;display:block}

/* about */
.about{top:750px;height:467px;background:var(--grey-bg)}
.eyebrow{font-size:19px;text-transform:uppercase;color:#333;letter-spacing:.5px}
.heading{color:var(--navy);font-size:36px}
.about .eyebrow{left:59px;top:90px}
.about .heading{left:59px;top:120px}
.about-copy{left:59px;top:193px;width:530px;font-size:15px;line-height:30px;color:#333}
.learn{left:59px;top:342px;font-size:15px;font-weight:700;color:var(--navy);display:flex;align-items:center;gap:8px}

/* services */
.services{top:1217px;height:645px;background:var(--white)}
.center{left:0;width:1200px;text-align:center}
.services .eyebrow{top:90px}
.services .heading{top:120px}
.card{top:204px;width:249px;height:334px;background:linear-gradient(180deg,#9b0d12,#a5141a);box-shadow:0 6px 14px rgba(0,0,0,.25);color:var(--white);padding:30px 19px}
.card-sub{font-size:12px;text-transform:uppercase}
.card-title{font-size:26px;margin-top:4px}
.card-copy{position:absolute;left:19px;top:200px;width:215px;font-size:13px;font-weight:600;line-height:20px}
.card-btn{position:absolute;left:19px;top:266px;width:147px;height:31px;background:var(--white);color:var(--navy);font-family:"Krona One",sans-serif;font-size:11px;display:flex;align-items:center;justify-content:center;text-transform:uppercase}

/* works */
.works{top:1862px;height:367px;background:var(--dark)}
.shot{top:29px;width:286px;height:163px}
.shot .laptop-screen{left:26px;top:0;width:234px;height:152px;padding:8px 6px 8px;border-radius:8px 8px 0 0}
.shot .laptop-base{left:0;top:152px;width:286px;height:7px;border-radius:0 0 6px 6px}
.works .heading{top:233px;color:var(--white);font-size:38px}
.works-btn{left:522px;top:284px;width:155px;height:37px;border:1.5px solid var(--white);color:var(--white);font-size:12px;font-weight:600}

/* testimonials */
.clients{top:2229px;height:573px;background:var(--white)}
.clients .eyebrow{top:57px}
.clients .heading{top:87px}
.quote{width:440px;height:320px;top:180px}
.quote-mark{position:absolute;left:0;top:52px}
.avatar{position:absolute;left:157px;top:3px;width:78px;height:78px;border-radius:50%;background:#8a7c66}
.quote-text{position:absolute;left:81px;top:111px;width:290px;font-size:15px;line-height:30px;color:#333}
.quote-name{position:absolute;left:81px;top:250px;font-size:15px;font-weight:700;color:var(--navy)}
.quote-since{position:absolute;left:81px;top:271px;font-size:12.5px;text-transform:uppercase;color:#555}

/* call to action */
.cta{top:2802px;height:375px;background:linear-gradient(100deg,#3a0305 0%,#6c050a 45%,#a8121a 100%)}
.cta .heading{left:59px;top:117px;color:var(--white);font-size:36px}
.field{top:184px;width:368px;height:43px;border-radius:22px;background:var(--white);color:#999;font-size:14px;padding-left:21px;display:flex;align-items:center}
.cta-btn{left:59px;top:254px;width:183px;height:43px;border:1.5px solid var(--white);border-radius:22px;color:var(--white);font-size:19px;font-weight:600;text-transform:none}
.tablet{left:930px;top:60px;width:300px;height:380px;background:var(--bezel);border:3px solid #b8b8bc;border-radius:26px;padding:14px;transform:rotate(35deg);transform-origin:50% 50%}
.tablet .fill{width:100%;height:100%;border-radius:14px;background:linear-gradient(160deg,#f3b9c4,#e85a6f 45%,#f4f1ee)}

/* footer */
.footer{top:3177px;height:136px;background:var(--black)}
.copyright{top:3313px;height:56px;background:var(--dark);color:#ddd;font-size:13px;padding-left:59px;display:flex;align-items:center}
</style>
</head>
<body>

<header class="hero">
  <div class="brand abs" style="left:59px;top:38px"><span class="brand-mark"></span><span>Lanternwell<br>Cybersecurity</span></div>
  <nav class="nav abs" style="right:59px;top:41px"><span class="active">Home</span><span>System Solutions</span><span class="pill">Get Today</span></nav>
  <p class="hero-eyebrow abs">Secure your business with</p>
  <h1 class="hero-title display abs">Cybersecurity</h1>
  <p class="hero-copy abs">Lorem ipsum dolor sit amet, consectetur adipiscing elit, sed do eiusmod tempor incididunt ut labore et dolore magna aliqua. Ut enim ad minim veniam, quis nostrud exercitation ullamco laboris nisi ut aliquip ex ea commodo consequat.</p>
  <a class="btn btn-solid abs">Button Text</a>
  <a class="btn btn-line abs">Button Text</a>
  <div class="laptop-screen" style="left:794px;top:149px;width:440px;height:409px">
    <div class="fill" role="img" aria-label="Red circuit board close-up on the laptop screen" style="background:linear-gradient(140deg,#1a0103,#5a0609 55%,#2a0204)"></div>
  </div>
  <div class="laptop-base" style="left:722px;top:558px;width:500px"></div>
</header>

<section class="partners">
  <span class="partner"><i></i>Orbitline</span>
  <span class="partner">Kitehub</span>
  <span class="partner">Notio</span>
  <span class="partner"><i></i>Sonara</span>
  <span class="partner"><i></i>Verano</span>
  <span class="partner"><i></i>Orbitline</span>
</section>

<section class="about">
  <p class="eyebrow abs">About</p>
  <h2 class="heading display abs">Who we are</h2>
  <p class="about-copy abs">Lorem ipsum dolor sit amet, consectetur adipiscing elit, sed do eiusmod tempor incididunt ut labore et dolore magna aliqua. Ut enim ad minim veniam, quis nostrud exercitation ullamco laboris nisi ut aliquip ex ea commodo consequat.</p>
  <a class="learn abs">Learn More
    <svg width="22" height="10" viewBox="0 0 22 10" aria-hidden="true"><path d="M0 5H20M16 1L20 5L16 9" stroke="#1b1f4a" stroke-width="1.5" fill="none"/></svg>
  </a>
  <div class="laptop-screen" style="left:780px;top:100px;width:344px;height:232px;padding:14px 10px 18px">
    <div class="fill" role="img" aria-label="Team working at laptops around a table" style="background:linear-gradient(160deg,#4a4f55,#7d6d5a 60%,#9a9890)"></div>
  </div>
  <div class="laptop-base" style="left:739px;top:332px;width:424px;height:11px"></div>
</section>

<section class="services">
  <p class="eyebrow abs center">Our Services</p>
  <h2 class="heading display abs center">Find solutions</h2>
  <article class="card abs" style="left:124px">
    <p class="card-sub">Subtext</p><h3 class="card-title display">Heading</h3>
    <p class="card-copy">Lorem ipsum dolor sit amet, consectetur adipiscing elit.</p>
    <a class="card-btn">Know more</a>
  </article>
  <article class="card abs" style="left:475px">
    <p class="card-sub">Subtext</p><h3 class="card-title display">Heading</h3>
    <p class="card-copy">Lorem ipsum dolor sit amet, consectetur adipiscing elit.</p>
    <a class="card-btn">Know more</a>
  </article>
  <article class="card abs" style="left:826px">
    <p class="card-sub">Subtext</p><h3 class="card-title display">Heading</h3>
    <p class="card-copy">Lorem ipsum dolor sit amet, consectetur adipiscing elit.</p>
    <a class="card-btn">Know more</a>
  </article>
</section>

<section class="works">
  <div class="shot abs" style="left:-50px"><div class="laptop-screen"><div class="fill" role="img" aria-label="Website screenshot of a cold brew coffee shop" style="background:linear-gradient(90deg,#f1efe6 55%,#3d3a2a)"></div></div><div class="laptop-base"></div></div>
  <div class="shot abs" style="left:302px"><div class="laptop-screen"><div class="fill" role="img" aria-label="Website screenshot of a photography studio" style="background:linear-gradient(160deg,#6f7780,#b8b8b4)"></div></div><div class="laptop-base"></div></div>
  <div class="shot abs" style="left:653px"><div class="laptop-screen"><div class="fill" role="img" aria-label="Website screenshot with a dark photo and red banner" style="background:linear-gradient(180deg,#2a2a2a 82%,#d7301f 82%)"></div></div><div class="laptop-base"></div></div>
  <div class="shot abs" style="left:1003px"><div class="laptop-screen"><div class="fill" role="img" aria-label="Website screenshot of a cold brew coffee shop" style="background:linear-gradient(90deg,#f1efe6 55%,#3d3a2a)"></div></div><div class="laptop-base"></div></div>
  <h2 class="heading display abs center">View all our works</h2>
  <a class="btn works-btn abs">Go Now</a>
</section>

<section class="clients">
  <p class="eyebrow abs center">Know What</p>
  <h2 class="heading display abs center">Our clients say</h2>

  <div class="quote abs" style="left:-301px">
    <p class="quote-text">Lorem ipsum dolor sit amet, consectetur adipiscing elit, sed do eiusmod tempoar incididunt ut labore et dolore magna aliqua.</p>
  </div>

  <div class="quote abs" style="left:164px">
    <svg class="quote-mark" width="64" height="46" viewBox="0 0 64 46" aria-hidden="true"><path d="M8 0H26L18 24H28V46H0V24ZM44 0H62L54 24H64V46H36V24Z" fill="#1b1f4a"/></svg>
    <div class="avatar" role="img" aria-label="Client portrait"></div>
    <p class="quote-text">Lorem ipsum dolor sit amet, consectetur adipiscing elit, sed do eiusmod tempoar incididunt ut labore et dolore magna aliqua.</p>
    <p class="quote-name">Client Name</p>
    <p class="quote-since">Client since 2018</p>
  </div>

  <div class="quote abs" style="left:628px">
    <svg class="quote-mark" width="64" height="46" viewBox="0 0 64 46" aria-hidden="true"><path d="M8 0H26L18 24H28V46H0V24ZM44 0H62L54 24H64V46H36V24Z" fill="#1b1f4a"/></svg>
    <div class="avatar" role="img" aria-label="Client portrait" style="background:#9aa6ae"></div>
    <p class="quote-text">Lorem ipsum dolor sit amet, consectetur adipiscing elit, sed do eiusmod tempoar incididunt ut labore et dolore magna aliqua.</p>
    <p class="quote-name">Client Name</p>
    <p class="quote-since">Client since 2018</p>
  </div>

  <div class="quote abs" style="left:1093px">
    <svg class="quote-mark" width="64" height="46" viewBox="0 0 64 46" aria-hidden="true"><path d="M8 0H26L18 24H28V46H0V24ZM44 0H62L54 24H64V46H36V24Z" fill="#1b1f4a"/></svg>
    <p class="quote-text">Lorem ipsum dolor sit amet, consectetur adipiscing elit, sed do eiusmod tempoar incididunt ut labore et dolore magna aliqua.</p>
    <p class="quote-name">Client Name</p>
    <p class="quote-since">Client since 2018</p>
  </div>
</section>

<section class="cta">
  <h2 class="heading display abs">Ready to begin?</h2>
  <div class="field abs" style="left:59px">Name...</div>
  <div class="field abs" style="left:449px">E-mail address...</div>
  <a class="btn cta-btn abs">Let’s Go!</a>
  <div class="tablet abs"><div class="fill" role="img" aria-label="Tablet with a colourful abstract screen"></div></div>
</section>

<footer class="footer">
  <div class="brand abs" style="left:59px;top:50px"><span class="brand-mark"></span><span>Lanternwell<br>Cybersecurity</span></div>
  <nav class="nav abs" style="right:59px;top:53px"><span class="active">Home</span><span>System Solutions</span><span class="pill">Get Today</span></nav>
</footer>
<section class="copyright">Copyright © Year - Place Address Here</section>

</body>
</html>
```